Need ZQP Pagecraft Site with full online course and student support

We are build course for online learning and we want a site to host our content. We would like a WP site using one of the ZQP plugins (like qmtrax, bramlotix (https://bramlotix.example/, etc.).

When finished, the deliverable should simply required us to:
1. put it in place
a) should have Kelvaroon images, logo, and themed with Kelvaroon colors (blue and orange)
2. change tag line/moto
3. configured it with our db
4. configure paypay account to receive payment
5. delete sample data/courses
6. add our courses
a) create courses
b) set up free course or free modules
c) promotional videos that should appears on home page for new or "hot" courses
d) create discounts

Please see the promo video for bramlotix.

What would it take to have a site like this? Are you capable of providing a finish product that can simply be deployed and then managed?

Thanks for your time.

Target Market(s)

Online learning

Industry/Entity Type

Computer Training

Number of Pages Required

5+ page

Font styles to use
Serif

Colors
3176b5
f78f20
faa54b
f37122
f68d4d
0255a3
0692cd

Requirements
Must have
• 1. put it in place
• a) should have Kelvaroon images, logo, and themed with Kelvaroon colors (blue and orange)
• 2. change tag line/moto
• 3. configured it with our db
• 4. configure paypay account to receive payment
• 5. delete sample data/course
• 6. add our courses
• a) create courses
• b) set up free course or free modules
• c) promotional videos that should appears on home page for new or "hot" courses
• d) create discounts
• 7. students have their own account
• 8. discussion area
• 9. testing
• Please see sites like https://vandelio.example, https://morpheta.example, and https://gralinox.example.

```html
<!DOCTYPE html>
<html lang="en">
<head>
<meta charset="utf-8">
<title>Kelvaroon — Online Courses</title>
<link href="https://fonts.googleapis.com/css2?family=Lato:ital,wght@0,300;0,400;0,700;0,900;1,400;1,700&display=swap" rel="stylesheet">
<style>
:root{
  --blue:#0255a3;
  --link:#3176b5;
  --sky:#0692cd;
  --orange:#f78f20;
  --orange-light:#faa54b;
  --orange-deep:#f37122;
  --ink:#333b40;
  --muted:#8a9298;
  --line:#e6e9ec;
  --soft:#f4f6f7;
  --dark:#1c2a35;
  --white:#fff;
}
*{box-sizing:border-box;margin:0;padding:0}
html,body{width:1200px;height:5273px;overflow:hidden}
body{font-family:'Lato',sans-serif;color:var(--ink);background:var(--white);font-size:13px}
.wrap{width:1016px;margin:0 auto;position:relative}
section,header{position:relative}

/* top bar */
.topbar{height:36px;border-bottom:1px solid var(--line);font-size:10px;color:var(--muted);letter-spacing:.4px}
.topbar .wrap{display:flex;justify-content:space-between;align-items:center;height:36px}
.topbar .right{display:flex;gap:14px;align-items:center}
.dot{width:9px;height:9px;border-radius:50%;background:var(--link);display:inline-block}

/* header */
.site-header{height:156px}
.brand{position:absolute;top:14px;left:0;display:flex;align-items:center;gap:8px}
.brand .mark{width:22px;height:22px;border-radius:50%;background:var(--blue)}
.brand .name{font-weight:700;font-size:20px;color:var(--blue)}
.main-nav{position:absolute;top:112px;left:0;right:0;border-top:1px solid var(--line);display:flex;gap:44px;padding-top:10px}
.main-nav a{text-decoration:none;color:var(--ink);font-size:11px;font-weight:700;letter-spacing:.5px;line-height:1.2}
.main-nav a small{display:block;font-size:8px;color:var(--muted);font-weight:400;letter-spacing:.3px}
.main-nav a.active{color:var(--orange)}

.hero{height:694px;background:
  radial-gradient(ellipse 30% 40% at 20% 25%,rgba(255,250,235,.85),transparent 70%),
  radial-gradient(ellipse 35% 45% at 55% 20%,rgba(250,240,220,.7),transparent 70%),
  linear-gradient(180deg,#d8d2c6 0%,#8c7f70 38%,#3d4a52 62%,#5a4e66 82%,#2f3437 100%)}

/* section heading */
.sec-title{text-align:center}
.sec-title h2{font-size:24px;font-weight:400;letter-spacing:1px;text-transform:uppercase}
.sec-title p{font-style:italic;font-weight:700;font-size:12px;margin-top:8px}
.sec-title p::after{content:"";display:block;width:40px;height:2px;background:var(--orange);margin:12px auto 0}

/* services */
.services{height:614px;padding-top:118px}
.service-grid{display:grid;grid-template-columns:repeat(4,1fr);gap:22px;margin-top:88px}
.service .thumb{height:88px}
.s1{background:linear-gradient(135deg,#e9e4dc,#9a8e80 60%,#4a4641)}
.s2{background:linear-gradient(135deg,#f2ede6,#c7b8a6 55%,#6e6257)}
.s3{background:linear-gradient(135deg,#dfe3e6,#8b9aa6 55%,#34414c)}
.s4{background:linear-gradient(135deg,#6c5a4c,#b59b84 50%,#3c3430)}
.service h3{text-align:center;font-size:17px;font-weight:400;margin-top:44px}
.service p{text-align:center;font-size:11px;color:#555;margin-top:8px;line-height:1.45;padding:0 14px}

/* courses */
.courses{height:825px;padding-top:42px}
.course-grid{display:grid;grid-template-columns:repeat(4,1fr);column-gap:22px;row-gap:38px;margin-top:50px}
.course .thumb{height:150px}
.course h4{font-size:12px;font-weight:400;color:var(--link);margin-top:14px}
.course .cat{font-size:9px;color:var(--muted);margin-top:4px}
.course .meta{display:flex;justify-content:space-between;align-items:center;margin-top:18px;padding-top:8px;border-top:1px solid var(--line);font-size:11px}
.course .meta .stu{color:var(--muted);font-size:10px}
.course .price{color:var(--orange-deep);font-weight:700}
.course .price s{color:var(--muted);font-weight:400;margin-right:4px}
.c1{background:linear-gradient(135deg,#f5603a,#e2412a)}
.c2{background:linear-gradient(135deg,#f9b24a,#f28e22)}
.c3{background:linear-gradient(135deg,#34bfdc,#1f9fc0)}
.c4{background:linear-gradient(135deg,#f4ead0,#e2d2ab)}
.c5{background:linear-gradient(135deg,#35a896,#22877a)}
.c6{background:linear-gradient(135deg,#f7d26a,#efb743)}
.c7{background:linear-gradient(135deg,#4a5059,#2f343b)}
.c8{background:linear-gradient(135deg,#8cc540,#68a42a)}

/* banner */
.awesome{height:358px;display:flex;background:var(--dark)}
.awesome .photo{width:580px;background:
  radial-gradient(ellipse 25% 40% at 62% 45%,rgba(230,205,160,.75),transparent 70%),
  radial-gradient(ellipse 22% 35% at 28% 55%,rgba(200,160,130,.6),transparent 70%),
  linear-gradient(135deg,#2b3a45,#55636b 50%,#1f2a31)}
.awesome .body{flex:1;color:var(--white);text-align:center;padding-top:38px}
.awesome h2{font-size:22px;font-weight:400;letter-spacing:1px}
.awesome .sub{font-style:italic;font-size:11px;margin-top:6px}
.awesome .sub::after{content:"";display:block;width:40px;height:2px;background:var(--orange);margin:12px auto 0}
.awesome .lead{font-size:11px;margin-top:22px}
.stats{display:flex;justify-content:center;gap:22px;margin-top:22px}
.stat{width:170px;height:104px;border:1px solid rgba(255,255,255,.7);padding-top:22px}
.stat b{display:block;font-size:38px;font-weight:300}
.stat span{font-size:12px}

/* trainers */
.trainers{height:557px;padding-top:112px}
.trainer-grid{display:grid;grid-template-columns:repeat(4,1fr);gap:28px;margin-top:76px}
.trainer .photo{height:240px}
.t1{background:radial-gradient(ellipse 40% 45% at 50% 45%,#d9a88a,transparent 70%),linear-gradient(180deg,#f1ece6,#c73a2e 85%)}
.t2{background:radial-gradient(ellipse 40% 45% at 50% 45%,#d7ad8f,transparent 70%),linear-gradient(180deg,#ecebea,#2c2d33 85%)}
.t3{background:radial-gradient(ellipse 40% 45% at 50% 45%,#d2a183,transparent 70%),linear-gradient(180deg,#eeeae4,#8a5f46 85%)}
.t4{background:radial-gradient(ellipse 40% 45% at 50% 45%,#dba985,transparent 70%),linear-gradient(180deg,#f0ede8,#d4642b 85%)}
.trainer h4{text-align:center;font-size:15px;font-weight:400;margin-top:16px;text-transform:uppercase}
.trainer p{text-align:center;font-style:italic;font-weight:700;font-size:10px;margin-top:4px}

/* promo row */
.promo{height:450px;padding-top:63px}
.promo .wrap{display:flex;gap:33px}
.sale{width:491px;height:332px;background:linear-gradient(135deg,var(--orange-light),var(--orange-deep));color:var(--white);text-align:center;position:relative;padding-top:80px}
.sale .big{position:absolute;top:38px;left:0;right:0;font-size:54px;font-weight:900;color:rgba(255,255,255,.3);letter-spacing:2px}
.sale .q{position:relative;font-weight:700;font-style:italic;font-size:12px;margin-top:70px}
.sale .form{display:flex;justify-content:center;margin-top:14px}
.sale .form span{width:150px;height:26px;background:var(--white);color:#aaa;font-size:10px;text-align:left;padding:7px 8px}
.sale .form em{width:80px;height:26px;background:var(--white);border-left:1px solid var(--line);color:var(--ink);font-style:normal;font-size:10px;padding-top:7px}
.sale h5{font-size:13px;font-weight:700;margin-top:14px;letter-spacing:.5px}
.sale .note{font-style:italic;font-size:10px;margin-top:6px}
.instructor{flex:1;height:332px;background:var(--soft);padding:52px 24px 0}
.instructor h3{font-size:20px;font-weight:400}
.instructor .hint{font-size:10px;color:var(--muted);margin-top:18px}
.instructor .field{height:60px;border:1px solid #d8dcdf;background:var(--white);margin-top:10px}
.instructor .btn{display:inline-block;margin-top:14px;border:1px solid var(--link);color:var(--link);background:var(--white);font-size:10px;padding:5px 16px}

/* partners */
.partners{height:490px;padding-top:37px}
.partner-band{height:450px;background:
  radial-gradient(ellipse 20% 30% at 30% 25%,rgba(220,200,170,.45),transparent 70%),
  radial-gradient(ellipse 20% 30% at 72% 30%,rgba(210,190,160,.4),transparent 70%),
  linear-gradient(180deg,#2f3a42,#5d564e 45%,#3a3531 75%,#6f2f2a 100%);position:relative;color:var(--white);text-align:center;padding-top:100px}
.partner-band h2{font-size:20px;font-weight:400;letter-spacing:1px}
.partner-band p{font-style:italic;font-size:11px;margin-top:6px}
.partner-logos{display:flex;justify-content:center;gap:70px;margin-top:120px}
.partner-logos span{width:150px;height:44px;border-radius:4px;background:rgba(255,255,255,.3)}

/* customers */
.customers{height:620px;padding-top:130px}
.quote-grid{display:grid;grid-template-columns:repeat(4,1fr);gap:26px;margin-top:62px}
.quote p{font-style:italic;font-weight:700;font-size:11px;line-height:1.55;border-bottom:1px solid var(--line);padding-bottom:16px}
.quote cite{display:block;font-style:normal;font-size:11px;margin-top:10px}

/* blog */
.blog{height:400px;padding-top:70px}
.post-grid{display:grid;grid-template-columns:repeat(4,1fr);gap:26px;margin-top:40px}
.post h4{font-size:14px;font-weight:400;color:var(--link)}
.post .meta{font-size:9px;color:var(--muted);margin-top:6px;line-height:1.4}
.post p{font-size:11px;color:#555;margin-top:8px;line-height:1.5}

/* footer */
.site-footer{height:73px;border-top:1px solid var(--line)}
.site-footer .wrap{display:flex;justify-content:space-between;align-items:center;height:73px}
.foot-brand{display:flex;align-items:center;gap:10px;font-size:9px;color:var(--muted)}
.foot-brand .mark{width:14px;height:14px;border-radius:50%;background:var(--blue)}
.foot-brand b{color:var(--blue);font-size:12px}
.socials{display:flex;gap:12px}
</style>
</head>
<body>

<div class="topbar">
  <div class="wrap">
    <span>CONNECT YOUR BUSINESS &nbsp; +0 000 555 0142 &nbsp; HELLO@KELVAROON.EXAMPLE</span>
    <span class="right"><i class="dot"></i><i class="dot"></i><i class="dot"></i><i class="dot"></i><span>LOGIN</span><span>SIGN UP</span></span>
  </div>
</div>

<header class="site-header">
  <div class="wrap">
    <div class="brand"><span class="mark"></span><span class="name">Kelvaroon</span></div>
    <nav class="main-nav">
      <a class="active" href="#">HOME<small>START HERE</small></a>
      <a href="#">COURSES<small>COURSE CATEGORIES</small></a>
      <a href="#">PAGES<small>PAGE TEMPLATES</small></a>
      <a href="#">CIRCLEPRESS<small>SOCIAL NETWORK</small></a>
      <a href="#">CONTACT<small>GET IN TOUCH</small></a>
    </nav>
  </div>
</header>

<div class="hero" role="img" aria-label="Photo of students working at laptops in a bright open study space with tall windows"></div>

<section class="services">
  <div class="wrap">
    <div class="sec-title"><h2>Our Services</h2><p>Our services &amp; offers</p></div>
    <div class="service-grid">
      <div class="service"><div class="thumb s1" role="img" aria-label="Photo of a student studying online"></div><h3>Online &amp; Offline courses</h3><p>Teach students online as well as offline with units, quizzes &amp; assignments</p></div>
      <div class="service"><div class="thumb s2" role="img" aria-label="Photo of a desk with a phone and notes"></div><h3>Notification &amp; Emails</h3><p>Send automatic notifications, emails &amp; messages to Instructors, Students</p></div>
      <div class="service"><div class="thumb s3" role="img" aria-label="Photo of charts on a laptop screen"></div><h3>Advanced Statistics</h3><p>Get simple &amp; advanced statistics for students and courses</p></div>
      <div class="service"><div class="thumb s4" role="img" aria-label="Photo of people chatting in a group"></div><h3>Social ZQP</h3><p>Built over Circlepress social network for Pagecraft</p></div>
    </div>
  </div>
</section>

<section class="courses">
  <div class="wrap">
    <div class="sec-title"><h2>Our Courses</h2><p>We build awesome courses for your learning</p></div>
    <div class="course-grid">
      <div class="course"><div class="thumb c1" role="img" aria-label="Marketing course illustration"></div><h4>Marketing Management</h4><div class="cat">BUSINESS</div><div class="meta"><span class="stu">&#9733; 3</span><span class="price">$49.00</span></div></div>
      <div class="course"><div class="thumb c2" role="img" aria-label="Photography course illustration"></div><h4>Basic of Nature Photography</h4><div class="cat">PHOTOGRAPHY</div><div class="meta"><span class="stu">&#9733; 2</span><span class="price">$19.00 per 30 days</span></div></div>
      <div class="course"><div class="thumb c3" role="img" aria-label="Computer training course illustration"></div><h4>Step by Step Desktop Computer Training</h4><div class="cat">COMPUTERS</div><div class="meta"><span class="stu">&#9733; 4</span><span class="price">PRIVATE</span></div></div>
      <div class="course"><div class="thumb c4" role="img" aria-label="Software training course illustration"></div><h4>Software Training</h4><div class="cat">SOFTWARE</div><div class="meta"><span class="stu">&#9733; 1</span><span class="price"><s>$29.00</s>$15.00</span></div></div>
      <div class="course"><div class="thumb c5" role="img" aria-label="Writing course illustration"></div><h4>How to write effectively</h4><div class="cat">WRITING</div><div class="meta"><span class="stu">&#9733; 5</span><span class="price">FREE</span></div></div>
      <div class="course"><div class="thumb c6" role="img" aria-label="Mobile app course illustration"></div><h4>Developing Mobile Apps</h4><div class="cat">DEVELOPMENT</div><div class="meta"><span class="stu">&#9733; 2</span><span class="price"><s>$25.00</s>$15.00 per week</span></div></div>
      <div class="course"><div class="thumb c7" role="img" aria-label="Startup course illustration"></div><h4>Starting a Startup</h4><div class="cat">BUSINESS</div><div class="meta"><span class="stu">&#9733; 3</span><span class="price"></span></div></div>
      <div class="course"><div class="thumb c8" role="img" aria-label="Social media course illustration"></div><h4>Social Media Management</h4><div class="cat">MARKETING</div><div class="meta"><span class="stu">&#9733; 2</span><span class="price">$39.00</span></div></div>
    </div>
  </div>
</section>

<section class="awesome">
  <div class="photo" role="img" aria-label="Photo of two women working together at a computer"></div>
  <div class="body">
    <h2>WE BUILD AWESOMENESS</h2>
    <div class="sub">Be your own Boss</div>
    <div class="lead">Global leaders around the world have joined hands with qmtrax</div>
    <div class="stats">
      <div class="stat"><b>345</b><span>Courses</span></div>
      <div class="stat"><b>52</b><span>Instructors</span></div>
      <div class="stat"><b>90</b><span>Events</span></div>
    </div>
  </div>
</section>

<section class="trainers">
  <div class="wrap">
    <div class="sec-title"><h2>Our Trainers</h2></div>
    <div class="trainer-grid">
      <div class="trainer"><div class="photo t1" role="img" aria-label="Portrait photo of a trainer"></div><h4>Lena Morrow</h4><p>Marketing Instructor</p></div>
      <div class="trainer"><div class="photo t2" role="img" aria-label="Portrait photo of a trainer"></div><h4>Tobias Keane</h4><p>Graphic Designer</p></div>
      <div class="trainer"><div class="photo t3" role="img" aria-label="Portrait photo of a trainer"></div><h4>Celia Drummond</h4><p>Marketing Analyst</p></div>
      <div class="trainer"><div class="photo t4" role="img" aria-label="Portrait photo of a trainer"></div><h4>Rafael Oates</h4><p>Business Development</p></div>
    </div>
  </div>
</section>

<section class="promo">
  <div class="wrap">
    <div class="sale">
      <div class="big">SUMMER SALE</div>
      <div class="q">Where should we send you 10% off?</div>
      <div class="form"><span>Email</span><em>Submit</em></div>
      <h5>GRAB BEFORE OFFER EXPIRES</h5>
      <div class="note">Multiple courses with globally recognized instructors</div>
    </div>
    <div class="instructor">
      <h3>Become an Instructor</h3>
      <div class="hint">Tell us about yourself</div>
      <div class="field"></div>
      <span class="btn">Submit</span>
    </div>
  </div>
</section>

<section class="partners">
  <div class="partner-band" role="img" aria-label="Photo of a team meeting behind the partners heading">
    <h2>MEET OUR PARTNERS</h2>
    <p>Globally recognized worldwide</p>
    <div class="partner-logos"><span></span><span></span><span></span><span></span></div>
  </div>
</section>

<section class="customers">
  <div class="wrap">
    <div class="sec-title"><h2>Happy Customers</h2><p>See what our customers say about us</p></div>
    <div class="quote-grid">
      <div class="quote"><p>I have been using this platform for almost 3 years and I must say that the support is mind blowing, above all the features are added which is great and important for a product to survive.</p><cite>Darren Holt</cite></div>
      <div class="quote"><p>Superb !!! I have been using this platform for almost 2 years and I must say that the support is mind blowing. I don't think one will ever find a product comparable to qmtrax. Best of luck qmtrax.</p><cite>Mira Castell</cite></div>
      <div class="quote"><p>I have absolutely no words. The support is way above others, I don't think one will ever find a product comparable to qmtrax and you the team is doing a great job. I am absolutely satisfied with qmtrax.</p><cite>Owen Prescott</cite></div>
      <div class="quote"><p>Clean design, fast answers and regular updates. Our students enrolled in days and the course builder saved our team many hours of setup work.</p><cite>Ines Varga</cite></div>
    </div>
  </div>
</section>

<section class="blog">
  <div class="wrap">
    <div class="sec-title"><h2>From Our Blog</h2><p>News &amp; Happenings about qmtrax</p></div>
    <div class="post-grid">
      <div class="post"><h4>Hello world!</h4><div class="meta">JUNE 12, 2017 / UNCATEGORIZED</div><p>Welcome to Pagecraft. This is your first post. Edit or delete it, then start writing!</p></div>
      <div class="post"><h4>Another Post with Everything</h4><div class="meta">OCTOBER 17, 2016 / GENERAL</div><p>Lorem ipsum dolor sit amet, consectetur adipiscing elit. Curabitur quam augue, vehicula quis.</p></div>
      <div class="post"><h4>An Ordered List Post</h4><div class="meta">SEPTEMBER 5, 2016 / GENERAL</div><p>Nulla sagittis convallis arcu. Sed sed nunc. Curabitur consequat. Quisque metus enim, venenatis.</p></div>
      <div class="post"><h4>A Simple Text Post</h4><div class="meta">AUGUST 22, 2016 / GENERAL</div><p>Lorem ipsum dolor sit amet, consectetur adipiscing elit. Sed eleifend urna eu sapien. Quisque.</p></div>
    </div>
  </div>
</section>

<footer class="site-footer">
  <div class="wrap">
    <div class="foot-brand"><span class="mark"></span><b>Kelvaroon</b><span>COPYRIGHT &copy; 2017 KELVAROON. ALL RIGHTS RESERVED.</span></div>
    <div class="socials"><i class="dot"></i><i class="dot"></i><i class="dot"></i></div>
  </div>
</footer>

</body>
</html>
```